Stonebay Towing Business Card

Towing
Accident towing
Mechanical breakdown
Insurance, salvage and recovery
4wd off road towing
Light & Heavy towing
8347 2516
24 hour business 7 days

Logo can be whole size on front

Industry/Entity Type

Towing/ transport

Contact Information for Business Card

The above

```html
<!DOCTYPE html>
<html lang="en">
<head>
<meta charset="utf-8">
<title>Stonebay Towing Business Card</title>
<link href="https://fonts.googleapis.com/css2?family=Bebas+Neue&family=Poppins:wght@400;700&display=swap" rel="stylesheet">
<style>
  :root {
    --bg: #3a3a3a;
    --red: #d41f26;
    --red-deep: #8e1317;
    --black: #060606;
    --white: #ffffff;
  }
  * { margin: 0; padding: 0; box-sizing: border-box; }
  html, body { width: 1200px; height: 689px; overflow: hidden; }
  body { background: var(--bg); position: relative; font-family: "Poppins", sans-serif; }

  .card {
    position: absolute;
    top: 200px;
    width: 510px;
    height: 292px;
    border-radius: 22px;
    overflow: hidden;
  }
  .card-front {
    left: 60px;
    background: linear-gradient(170deg, var(--red) 0%, var(--red-deep) 50%, var(--black) 100%);
    display: flex;
    align-items: center;
    justify-content: center;
  }
  .brand-name {
    font-family: "Bebas Neue", sans-serif;
    font-size: 74px;
    letter-spacing: 2px;
    color: var(--black);
    line-height: 1;
  }

  .card-back { left: 630px; background: var(--red); }
  .back-shapes { position: absolute; inset: 0; width: 100%; height: 100%; }

  .contact {
    position: absolute;
    top: 26px;
    right: 30px;
    width: 240px;
    text-align: center;
    color: var(--white);
  }
  .phone-icon {
    width: 38px; height: 38px;
    margin: 0 auto 6px;
    display: block;
  }
  .phone-number { font-weight: 700; font-size: 40px; line-height: 1.05; }
  .hours { font-size: 17px; line-height: 1.2; }

  .services {
    position: absolute;
    left: 26px;
    bottom: 18px;
    list-style: none;
  }
  .service {
    display: flex;
    align-items: center;
    gap: 9px;
    font-family: "Bebas Neue", sans-serif;
    font-size: 21px;
    color: var(--white);
    letter-spacing: 0.5px;
    line-height: 1.12;
  }
  .service-icon { width: 16px; height: 16px; flex: none; }
</style>
</head>
<body>
  <section class="card card-front">
    <h1 class="brand-name">Stonebay Towing</h1>
  </section>

  <section class="card card-back">
    <svg class="back-shapes" viewBox="0 0 510 292" preserveAspectRatio="none" aria-hidden="true">
      <polygon points="0,98 510,214 510,292 0,292" fill="var(--black)"/>
      <polygon points="0,114 510,230 510,242 0,126" fill="var(--red)"/>
      <polygon points="250,150 470,200 460,208 240,158" fill="var(--red)"/>
    </svg>

    <div class="contact">
      <svg class="phone-icon" viewBox="0 0 38 38" aria-hidden="true">
        <circle cx="19" cy="19" r="19" fill="var(--black)"/>
        <path d="M11 15c4-4 12-4 16 0l-2.5 2.5-3-1.5v-2a9 9 0 0 0-5 0v2l-3 1.5z" fill="var(--white)"/>
      </svg>
      <p class="phone-number">8347 2516</p>
      <p class="hours">24 hour business<br>7 days</p>
    </div>

    <ul class="services">
      <li class="service"><svg class="service-icon" viewBox="0 0 16 16" aria-hidden="true"><circle cx="8" cy="8" r="6.5" fill="none" stroke="var(--red)" stroke-width="1.6"/><rect x="5.5" y="5.5" width="5" height="5" fill="var(--red)"/></svg>Towing</li>
      <li class="service"><svg class="service-icon" viewBox="0 0 16 16" aria-hidden="true"><circle cx="8" cy="8" r="6.5" fill="none" stroke="var(--red)" stroke-width="1.6"/><rect x="5.5" y="5.5" width="5" height="5" fill="var(--red)"/></svg>Accident Towing</li>
      <li class="service"><svg class="service-icon" viewBox="0 0 16 16" aria-hidden="true"><circle cx="8" cy="8" r="6.5" fill="none" stroke="var(--red)" stroke-width="1.6"/><rect x="5.5" y="5.5" width="5" height="5" fill="var(--red)"/></svg>Mechanical Breakdown</li>
      <li class="service"><svg class="service-icon" viewBox="0 0 16 16" aria-hidden="true"><circle cx="8" cy="8" r="6.5" fill="none" stroke="var(--red)" stroke-width="1.6"/><rect x="5.5" y="5.5" width="5" height="5" fill="var(--red)"/></svg>Insurance, Salvage and Recovery</li>
      <li class="service"><svg class="service-icon" viewBox="0 0 16 16" aria-hidden="true"><circle cx="8" cy="8" r="6.5" fill="none" stroke="var(--red)" stroke-width="1.6"/><rect x="5.5" y="5.5" width="5" height="5" fill="var(--red)"/></svg>4WD Off Road Towing</li>
      <li class="service"><svg class="service-icon" viewBox="0 0 16 16" aria-hidden="true"><circle cx="8" cy="8" r="6.5" fill="none" stroke="var(--red)" stroke-width="1.6"/><rect x="5.5" y="5.5" width="5" height="5" fill="var(--red)"/></svg>Light &amp; Heavy Towing</li>
    </ul>
  </section>
</body>
</html>
```